6 Product labels for a Skincare brand

I have a logo and 6 label templates for 6 skincare productsI need someone to design the product labelsthe design of all 6 labels should be very similar just with basic adjustmentsPlease show me only the design for "Velaquin30ml_Template_V2" and then we can do the others

Target Market(s)

Women +45

Industry/Entity Type

Skin Care Product

Font styles to use
Other font styles liked:
• Helvetica

Colors
ffffff
fef7ee
feeeee
fbe7d2
fefced

Requirements
Must have
• Clean Clean design
• Company details are:
• Distributed by: MARLEE QUINTAV, Denver, CO 80000
• support@marleequintav.example, (866) 555-0172

```html
<!DOCTYPE html>
<html lang="en">
<head>
<meta charset="utf-8">
<title>Velaquin 30 ml Label</title>
<link rel="stylesheet" href="https://fonts.googleapis.com/css2?family=Marcellus&family=Roboto:wght@300;400&display=swap">
<style>
  :root {
    --page: #ffffff;
    --label-white: #fdfdfc;
    --label-shade: #eeeeec;
    --peach: #f2cfa8;
    --peach-deep: #ecc498;
    --ink: #1c1c1c;
    --rule: #2a2a2a;
  }
  * { margin: 0; padding: 0; box-sizing: border-box; }
  html, body {
    width: 1200px;
    height: 975px;
    overflow: hidden;
    background: var(--page);
  }
  .canvas {
    position: relative;
    width: 1200px;
    height: 975px;
  }
  .label {
    position: absolute;
    left: 100px;
    top: 320px;
    width: 1000px;
    height: 334px;
    background: linear-gradient(180deg, var(--label-white) 0%, #f7f7f6 55%, var(--label-shade) 100%);
    box-shadow: 0 0 0 1px #ececec;
  }
  .label__edge {
    position: absolute;
    top: 0;
    width: 48px;
    height: 100%;
    background: linear-gradient(90deg, var(--peach-deep), var(--peach));
  }
  .label__edge--left { left: 0; }
  .label__edge--right { right: 0; background: linear-gradient(90deg, var(--peach), var(--peach-deep)); }

  .brand {
    position: absolute;
    left: 80px;
    top: 66px;
    width: 172px;
    height: 114px;
    display: flex;
    flex-direction: column;
    justify-content: center;
    align-items: center;
    border-top: 1.5px solid var(--rule);
    border-bottom: 1.5px solid var(--rule);
  }
  .brand__name {
    font-family: "Marcellus", serif;
    font-weight: 400;
    font-size: 26px;
    line-height: 1.35;
    letter-spacing: 5px;
    color: var(--ink);
    text-align: center;
  }

  .product {
    position: absolute;
    right: 78px;
    top: 140px;
    text-align: right;
    color: var(--ink);
    font-family: "Roboto", Helvetica, Arial, sans-serif;
  }
  .product__name {
    font-weight: 300;
    font-size: 68px;
    line-height: 1;
    letter-spacing: 6px;
    margin-right: -6px;
  }
  .product__tagline {
    font-weight: 400;
    font-size: 31px;
    line-height: 1;
    margin-top: 20px;
  }
  .product__volume {
    font-weight: 400;
    font-size: 21px;
    line-height: 1;
    margin-top: 22px;
  }
</style>
</head>
<body>
  <main class="canvas">
    <section class="label">
      <div class="label__edge label__edge--left"></div>
      <div class="label__edge label__edge--right"></div>

      <div class="brand">
        <p class="brand__name">MARLEE<br>QUINTAV</p>
      </div>

      <div class="product">
        <h1 class="product__name">VELAQUIN</h1>
        <p class="product__tagline">Loremp ipsum dolor sit</p>
        <p class="product__volume">30 ml | 1 fl oz</p>
      </div>
    </section>
  </main>
</body>
</html>
```